Book cover design for a book named BLOOM

Hello Designers,
The name of the book is BLOOM and it is about unexpected experiences individuals have which are beyond their control. Occurrences they are unable to overcome or get out of themselves without the help of God. After overcoming these situations they know only God could have done this for them, no one else could have. It is an adult Christian book. I would like you to be as creative as you can with the cover, using color, light, graphic designs, shapes, scale, lines etc. (you are the designers, I don't know how to do these things.) I would like to use the image created on a paperback, hardcover or e book. I tried to use an image from Pixmarble just to give you some idea of my thinking but you do not have to use these hands. The hands should look as if they are giving someone the word TESTIMONY not receiving it. Use of the words provided, the light rays, and some type of hands extended should not change, but how you use them is up to you. Use the words, light rays, and hands however you wish as long as they convey someone giving the word TESTIMONY. The word TESTIMONY should be proportional to the hand in size and should appear as if being held in the actual hand it should not be larger than the book name. It is a Christian book of testimonies. Also for your design samples you can use the name Marlene Quiller for the author. Thank you, please feel free to contact me if you have any questions. I am looking for the cover to be an attention grabber and give the reader something to really think about and remember visually when they see this cover. Thank you again.

Target Market(s)

anyone and christians

Requirements
Must have
• Use of the words provided, the light rays, and some type of hands extended should not change.
Nice to have
• be as creative as you can with the cover, using color, light, graphic designs, shapes, scale, lines etc. (you are the designers, I don't know how to do these things.)
Should not have
• It should not have fonts, colors, etc. that convey it is a child's book, fairytale, or fictional etc. It is a book of true stories that actually happened. It should not look exactly like my example, what I provided.

```html
<!DOCTYPE html>
<html lang="en">
<head>
<meta charset="utf-8">
<title>BLOOM – Book Cover</title>
<link rel="stylesheet" href="https://fonts.googleapis.com/css2?family=Cinzel:wght@400;500&family=Oswald:wght@400;700&family=Tinos:ital,wght@1,700&display=swap">
<style>
  :root {
    --backdrop: #444444;
    --title-orange: #e0782f;
    --band-orange: #d9622a;
    --band-orange-light: #e57e36;
    --ink-dark: #2e2a26;
    --ink-black: #111111;
    --paper-white: #ffffff;
    --rule: #3a332c;
  }
  * { margin: 0; padding: 0; box-sizing: border-box; }
  html, body {
    width: 1200px;
    height: 1200px;
    overflow: hidden;
    background: var(--backdrop);
  }
  .book-cover {
    position: absolute;
    left: 204px;
    top: 18px;
    width: 773px;
    height: 1158px;
    overflow: hidden;
  }
  .cover-art {
    position: absolute;
    inset: 0;
    width: 100%;
    height: 100%;
  }
  .book-title {
    position: absolute;
    top: 104px;
    width: 100%;
    text-align: center;
    font-family: "Cinzel", serif;
    font-weight: 400;
    font-size: 162px;
    line-height: 1;
    letter-spacing: 1px;
    color: var(--title-orange);
  }
  .tagline {
    position: absolute;
    top: 320px;
    width: 100%;
    text-align: center;
    font-family: "Tinos", serif;
    font-style: italic;
    font-weight: 700;
    font-size: 21px;
    line-height: 38px;
    color: var(--ink-black);
  }
  .rule {
    position: absolute;
    left: 144px;
    width: 485px;
    height: 2px;
    background: linear-gradient(90deg, transparent, var(--rule) 25%, var(--rule) 75%, transparent);
  }
  .rule--top { top: 294px; }
  .rule--bottom { top: 407px; }
  .promise {
    position: absolute;
    top: 490px;
    width: 100%;
    text-align: center;
    font-family: "Oswald", sans-serif;
    font-weight: 400;
    font-size: 31px;
    line-height: 46px;
    letter-spacing: 2px;
    color: var(--ink-dark);
  }
  .promise-word {
    position: absolute;
    top: 646px;
    width: 100%;
    padding-right: 14px;
    text-align: center;
    font-family: "Oswald", sans-serif;
    font-weight: 700;
    font-style: italic;
    font-size: 82px;
    line-height: 1;
    letter-spacing: 0;
    color: var(--ink-black);
  }
  .author {
    position: absolute;
    top: 1060px;
    width: 100%;
    text-align: center;
    font-family: "Cinzel", serif;
    font-weight: 500;
    font-size: 50px;
    line-height: 1;
    letter-spacing: 1px;
    color: var(--paper-white);
  }
</style>
</head>
<body>
  <main class="book-cover">
    <svg class="cover-art" viewBox="0 0 773 1158" preserveAspectRatio="none">
      <defs>
        <linearGradient id="sky" x1="0" y1="0" x2="0" y2="1">
          <stop offset="0" stop-color="#cbdbe0"/>
          <stop offset="0.22" stop-color="#fbf5e6"/>
          <stop offset="0.45" stop-color="#fcedc4"/>
          <stop offset="0.6" stop-color="#f6cf83"/>
          <stop offset="0.72" stop-color="#e9a257"/>
          <stop offset="0.85" stop-color="#b8743e"/>
          <stop offset="1" stop-color="#6e4a33"/>
        </linearGradient>
        <radialGradient id="glow" cx="390" cy="800" r="260" gradientUnits="userSpaceOnUse">
          <stop offset="0" stop-color="#fffbe8"/>
          <stop offset="0.3" stop-color="#fff1c0" stop-opacity="0.8"/>
          <stop offset="1" stop-color="#ffe2a0" stop-opacity="0"/>
        </radialGradient>
        <radialGradient id="hands-tone" cx="390" cy="900" r="230" gradientUnits="userSpaceOnUse" gradientTransform="translate(390 900) scale(1 1.4) translate(-390 -900)">
          <stop offset="0" stop-color="#5a3a28" stop-opacity="0.45"/>
          <stop offset="1" stop-color="#5a3a28" stop-opacity="0"/>
        </radialGradient>
        <radialGradient id="ray-fade" cx="390" cy="800" r="330" gradientUnits="userSpaceOnUse">
          <stop offset="0" stop-color="#ffffff" stop-opacity="0.95"/>
          <stop offset="1" stop-color="#ffffff" stop-opacity="0"/>
        </radialGradient>
        <linearGradient id="band" x1="0" y1="0" x2="1" y2="0">
          <stop offset="0" stop-color="var(--band-orange)"/>
          <stop offset="1" stop-color="var(--band-orange-light)"/>
        </linearGradient>
      </defs>
      <g role="img" aria-label="Photograph of two open hands extended upward against a glowing sunset sky over the sea, offering light that bursts between them">
        <rect width="773" height="1158" fill="url(#sky)"/>
        <rect width="773" height="1158" fill="url(#hands-tone)"/>
        <rect width="773" height="1158" fill="url(#glow)"/>
      </g>
      <g class="light-rays" stroke="url(#ray-fade)" stroke-linecap="round">
        <line x1="390" y1="800" x2="390" y2="500" stroke-width="4"/>
        <line x1="390" y1="800" x2="300" y2="520" stroke-width="3"/>
        <line x1="390" y1="800" x2="480" y2="520" stroke-width="3"/>
        <line x1="390" y1="800" x2="220" y2="580" stroke-width="2.5"/>
        <line x1="390" y1="800" x2="560" y2="580" stroke-width="2.5"/>
        <line x1="390" y1="800" x2="150" y2="680" stroke-width="2"/>
        <line x1="390" y1="800" x2="630" y2="680" stroke-width="2"/>
        <line x1="390" y1="800" x2="110" y2="800" stroke-width="2"/>
        <line x1="390" y1="800" x2="670" y2="800" stroke-width="2"/>
        <line x1="390" y1="800" x2="170" y2="920" stroke-width="1.5"/>
        <line x1="390" y1="800" x2="610" y2="920" stroke-width="1.5"/>
        <line x1="390" y1="800" x2="345" y2="560" stroke-width="1.5"/>
        <line x1="390" y1="800" x2="435" y2="560" stroke-width="1.5"/>
        <line x1="390" y1="800" x2="260" y2="620" stroke-width="1.5"/>
        <line x1="390" y1="800" x2="520" y2="620" stroke-width="1.5"/>
      </g>
      <circle class="light-core" cx="390" cy="800" r="26" fill="#fffdf2" opacity="0.9"/>
      <path class="footer-band" d="M0 1038 C 220 1056, 520 1022, 773 892 L773 1158 L0 1158 Z" fill="url(#band)"/>
    </svg>

    <h1 class="book-title">BLOOM</h1>
    <div class="rule rule--top"></div>
    <p class="tagline">Before there will ever be a TESTIMONY there<br>Must always be an experience.</p>
    <div class="rule rule--bottom"></div>
    <p class="promise">OUT OF THE TEST I’VE GIVEN YOU<br>A</p>
    <p class="promise-word">TESTIMONY</p>
    <p class="author">MARLENE QUILLER</p>
  </main>
</body>
</html>
```